Velmorfood

We produce juices. We need a label design for 300ml and 1L bottles. Our company's name is "Velmor food", In honor of Aragats mountain. If we like some of the examples, in future for the final result we will send Armenian version of company's name in armenian letters.

Industry/Entity Type

It Company

```html
<!DOCTYPE html>
<html lang="en">
<head>
<meta charset="utf-8">
<title>Velmor food – Juice Labels</title>
<link rel="stylesheet" href="https://fonts.googleapis.com/css2?family=Bitter:wght@800&display=swap">
<style>
  :root {
    --canvas-bg: #ffffff;
    --orange-glass-light: #ffc21a;
    --orange-glass-dark: #f07f1c;
    --kiwi-glass-light: #4cc04a;
    --kiwi-glass-dark: #1f8e34;
    --cap: #e0cf98;
    --frame-gold: #e8b92e;
    --frame-green: #78b82a;
    --label-cream: #fffbe2;
    --label-yellow: #fbe27a;
    --ribbon-orange-light: #fcb23b;
    --ribbon-orange-dark: #ef7c1d;
    --ribbon-green: #3f9a2a;
    --title-fill: #ffffff;
    --title-outline: #d8321e;
    --brand-green: #6aa61c;
    --orange-fruit-light: #ffd24a;
    --orange-fruit-dark: #f59a17;
    --kiwi-fruit-light: #f4f7d8;
    --kiwi-fruit-dark: #6cb02b;
    --shadow: #e9e9e9;
  }
  html, body {
    margin: 0;
    padding: 0;
    width: 1200px;
    height: 946px;
    overflow: hidden;
    background: var(--canvas-bg);
  }
  .label-sheet {
    display: block;
    width: 1200px;
    height: 946px;
  }
  .brand-name {
    font-family: "Bitter", Georgia, serif;
    font-weight: 800;
    font-size: 30px;
    fill: var(--brand-green);
  }
  .product-title {
    font-family: "Bitter", Georgia, serif;
    font-weight: 800;
    font-size: 33px;
    fill: var(--title-fill);
    stroke: var(--title-outline);
    stroke-width: 5px;
    paint-order: stroke;
    stroke-linejoin: round;
  }
</style>
</head>
<body>
<svg class="label-sheet" viewBox="0 0 1200 946" xmlns="http://www.w3.org/2000/svg">
  <defs>
    <linearGradient id="orange-glass" x1="0" x2="1">
      <stop offset="0" stop-color="var(--orange-glass-dark)"/>
      <stop offset="0.6" stop-color="var(--orange-glass-light)"/>
      <stop offset="1" stop-color="var(--orange-glass-dark)"/>
    </linearGradient>
    <linearGradient id="kiwi-glass" x1="0" x2="1">
      <stop offset="0" stop-color="var(--kiwi-glass-dark)"/>
      <stop offset="0.45" stop-color="var(--kiwi-glass-light)"/>
      <stop offset="1" stop-color="var(--kiwi-glass-dark)"/>
    </linearGradient>
    <linearGradient id="label-face" x1="0" y1="0" x2="0" y2="1">
      <stop offset="0" stop-color="var(--label-yellow)"/>
      <stop offset="0.45" stop-color="var(--label-cream)"/>
      <stop offset="1" stop-color="var(--label-yellow)"/>
    </linearGradient>
    <linearGradient id="label-frame" x1="0" y1="0" x2="1" y2="1">
      <stop offset="0" stop-color="var(--frame-green)"/>
      <stop offset="0.5" stop-color="var(--frame-gold)"/>
      <stop offset="1" stop-color="var(--frame-gold)"/>
    </linearGradient>
    <linearGradient id="ribbon-band" x1="0" y1="0" x2="0" y2="1">
      <stop offset="0" stop-color="var(--ribbon-orange-light)"/>
      <stop offset="1" stop-color="var(--ribbon-orange-dark)"/>
    </linearGradient>
    <radialGradient id="orange-slice">
      <stop offset="0" stop-color="var(--orange-fruit-light)"/>
      <stop offset="1" stop-color="var(--orange-fruit-dark)"/>
    </radialGradient>
    <radialGradient id="kiwi-slice">
      <stop offset="0.2" stop-color="var(--kiwi-fruit-light)"/>
      <stop offset="1" stop-color="var(--kiwi-fruit-dark)"/>
    </radialGradient>
    <clipPath id="label-inner">
      <ellipse cx="0" cy="0" rx="106" ry="156"/>
    </clipPath>
  </defs>

  <!-- bottle shadows -->
  <ellipse class="floor-shadow" cx="147" cy="790" rx="128" ry="14" fill="var(--shadow)"/>
  <ellipse class="floor-shadow" cx="752" cy="786" rx="128" ry="14" fill="var(--shadow)"/>

  <!-- orange bottle -->
  <g class="bottle bottle--orange" role="img" aria-label="Illustration of an orange glass juice bottle with a gold crown cap">
    <rect x="88" y="58" width="112" height="28" rx="6" fill="var(--cap)"/>
    <rect x="20" y="84" width="255" height="696" rx="40" fill="url(#orange-glass)"/>
  </g>

  <!-- kiwi bottle -->
  <g class="bottle bottle--kiwi" role="img" aria-label="Illustration of a green glass juice bottle with a gold crown cap">
    <rect x="698" y="54" width="110" height="28" rx="6" fill="var(--cap)"/>
    <rect x="625" y="80" width="255" height="696" rx="40" fill="url(#kiwi-glass)"/>
  </g>

  <!-- label: orange on bottle -->
  <g class="juice-label juice-label--orange" transform="translate(150 497)">
    <ellipse rx="116" ry="166" fill="url(#label-frame)"/>
    <ellipse rx="106" ry="156" fill="url(#label-face)"/>
    <g clip-path="url(#label-inner)">
      <circle class="fruit-slice" cx="0" cy="58" r="104" fill="url(#orange-slice)" role="img" aria-label="Illustration of a halved orange slice"/>
    </g>
    <circle cx="-78" cy="-71" r="6" fill="var(--brand-green)"/>
    <text class="brand-name" x="6" y="-60" text-anchor="middle">Velmor food</text>
    <g class="ribbon" transform="rotate(-13)">
      <polygon points="-150,-18 -120,-18 -120,42 -150,42 -136,12" fill="var(--ribbon-green)"/>
      <polygon points="150,-18 120,-18 120,42 150,42 136,12" fill="var(--ribbon-green)"/>
      <rect x="-132" y="-30" width="264" height="60" fill="url(#ribbon-band)"/>
      <text class="product-title" x="0" y="12" text-anchor="middle">Orange Juice</text>
    </g>
  </g>

  <!-- label: orange standalone -->
  <g class="juice-label juice-label--orange" transform="translate(437 493)">
    <ellipse rx="116" ry="166" fill="url(#label-frame)"/>
    <ellipse rx="106" ry="156" fill="url(#label-face)"/>
    <g clip-path="url(#label-inner)">
      <circle class="fruit-slice" cx="0" cy="58" r="104" fill="url(#orange-slice)" role="img" aria-label="Illustration of a halved orange slice"/>
    </g>
    <circle cx="-78" cy="-71" r="6" fill="var(--brand-green)"/>
    <text class="brand-name" x="6" y="-60" text-anchor="middle">Velmor food</text>
    <g class="ribbon" transform="rotate(-13)">
      <polygon points="-150,-18 -120,-18 -120,42 -150,42 -136,12" fill="var(--ribbon-green)"/>
      <polygon points="150,-18 120,-18 120,42 150,42 136,12" fill="var(--ribbon-green)"/>
      <rect x="-132" y="-30" width="264" height="60" fill="url(#ribbon-band)"/>
      <text class="product-title" x="0" y="12" text-anchor="middle">Orange Juice</text>
    </g>
  </g>

  <!-- label: kiwi on bottle -->
  <g class="juice-label juice-label--kiwi" transform="translate(755 505)">
    <ellipse rx="116" ry="166" fill="url(#label-frame)"/>
    <ellipse rx="106" ry="156" fill="url(#label-face)"/>
    <g clip-path="url(#label-inner)">
      <circle class="fruit-slice" cx="0" cy="58" r="104" fill="url(#kiwi-slice)" role="img" aria-label="Illustration of a halved kiwi slice"/>
    </g>
    <circle cx="-78" cy="-71" r="6" fill="var(--brand-green)"/>
    <text class="brand-name" x="6" y="-60" text-anchor="middle">Velmor food</text>
    <g class="ribbon" transform="rotate(-13)">
      <polygon points="-150,-18 -120,-18 -120,42 -150,42 -136,12" fill="var(--ribbon-green)"/>
      <polygon points="150,-18 120,-18 120,42 150,42 136,12" fill="var(--ribbon-green)"/>
      <rect x="-132" y="-30" width="264" height="60" fill="url(#ribbon-band)"/>
      <text class="product-title" x="0" y="12" text-anchor="middle">Kiwi Juice</text>
    </g>
  </g>

  <!-- label: kiwi standalone -->
  <g class="juice-label juice-label--kiwi" transform="translate(1050 490)">
    <ellipse rx="116" ry="166" fill="url(#label-frame)"/>
    <ellipse rx="106" ry="156" fill="url(#label-face)"/>
    <g clip-path="url(#label-inner)">
      <circle class="fruit-slice" cx="0" cy="58" r="104" fill="url(#kiwi-slice)" role="img" aria-label="Illustration of a halved kiwi slice"/>
    </g>
    <circle cx="-78" cy="-71" r="6" fill="var(--brand-green)"/>
    <text class="brand-name" x="6" y="-60" text-anchor="middle">Velmor food</text>
    <g class="ribbon" transform="rotate(-13)">
      <polygon points="-150,-18 -120,-18 -120,42 -150,42 -136,12" fill="var(--ribbon-green)"/>
      <polygon points="150,-18 120,-18 120,42 150,42 136,12" fill="var(--ribbon-green)"/>
      <rect x="-132" y="-30" width="264" height="60" fill="url(#ribbon-band)"/>
      <text class="product-title" x="0" y="12" text-anchor="middle">Kiwi Juice</text>
    </g>
  </g>
</svg>
</body>
</html>
```